Re-branding stationary for Company

Orvane Diamonds is a diamond trading company that has been established since more then 30years.

We are currently looking to re-design our current logo design into something more modern and more appealing the the new generation. Small changes are what we are looking for that will give our company a little more modern look and a new appeal.
The design should be on similar lines to what our current logo is, but we are definitely wanting to have some modern changes to this.
Along with this, we are looking to have design for complete stationary including, business cards, envelopes, letterheads, etc..

Attached is our current logo, can use this as a base point towards creating a new design.
Updates

Project Deadline Extended Reason: Am still looking for wonderful and amazingly creative design for my company, a facelift with a little modern touchHave provided you with a current logo of the company as inspiration to make something new and unique. PLEASE DO NOT USE COPY THE LOGO FILE AS IT IS! Added Wednesday, May 6, 2015

Target Market(s)

We are a company established since over 30 years, and want to maintain our core fundamental values which is portrayed through our logo. Use this as a base into creating new modern design.

Industry/Entity Type

It Company

Font styles to use
Serif
Sans Serif
Decorative
Script

Requirements
Must have
• A modern touch
• Color combination should be similar in terms with what we currently use in attached design.
Nice to have
• Want that the design is appealing using simple but yet modern features to change and restructure the current company logo.
Should not have
• Not looking more multi colored design
• Not gotta be too overly extravagant

```html
<!DOCTYPE html>
<html lang="en">
<head>
<meta charset="utf-8">
<title>Orvane Diamonds – Business Card</title>
<link rel="stylesheet" href="https://fonts.googleapis.com/css2?family=PT+Sans:wght@400;700&display=swap">
<style>
  :root {
    --navy: #2b3577;
    --ink: #3c3c3c;
    --grey-line: #9a9a9a;
    --card: #f4f4f4;
    --card-edge: #e2e2e2;
    --stage: #d9d9d9;
    --band: #c9c9c9;
  }
  * { margin: 0; padding: 0; box-sizing: border-box; }
  html, body { width: 1200px; height: 900px; overflow: hidden; }
  body {
    background: var(--stage);
    font-family: "PT Sans", sans-serif;
    color: var(--ink);
    position: relative;
  }
  .card {
    position: absolute;
    left: 300px;
    width: 600px;
    height: 343px;
    background: var(--card);
    border: 1px solid var(--card-edge);
    box-shadow: 0 6px 18px rgba(0,0,0,0.18);
    overflow: hidden;
  }
  .card--back { top: 70px; }
  .card--front { top: 480px; }

  .brand { display: flex; align-items: center; gap: 12px; }
  .brand__dot { border-radius: 50%; background: var(--navy); flex: none; }
  .brand__name { color: var(--navy); font-weight: 700; letter-spacing: 0.04em; text-transform: uppercase; line-height: 1; }
  .brand__tagline { font-size: 10px; color: var(--ink); margin-top: 4px; }
  .brand__suffix { font-size: 10px; color: var(--ink); text-align: right; }

  .card--back .brand {
    position: absolute; left: 50%; top: 50%;
    transform: translate(-50%, -50%);
  }
  .card--back .brand__dot { width: 44px; height: 44px; }
  .card--back .brand__name { font-size: 34px; }
  .card--back .brand__tagline { font-size: 12px; }
  .card--back .brand__suffix { font-size: 12px; }

  .card--front .brand { position: absolute; left: 38px; top: 36px; }
  .card--front .brand__dot { width: 30px; height: 30px; }
  .card--front .brand__name { font-size: 22px; }

  .divider { position: absolute; left: 38px; right: 38px; top: 178px; height: 1px; background: var(--grey-line); }

  .contact { position: absolute; left: 38px; top: 196px; list-style: none; font-size: 14px; line-height: 22px; }
  .contact li { display: flex; align-items: center; gap: 8px; }
  .contact svg { width: 12px; height: 12px; fill: var(--navy); flex: none; }

  .person { position: absolute; right: 38px; top: 196px; text-align: right; }
  .person__name { color: var(--navy); font-weight: 700; font-size: 15px; letter-spacing: 0.03em; line-height: 20px; }
  .person__role { font-size: 14px; line-height: 20px; }
  .person__rule { width: 240px; height: 1px; background: var(--grey-line); margin: 4px 0 0 auto; }
  .address { position: absolute; right: 38px; top: 250px; text-align: right; font-size: 14px; line-height: 20px; }

  .stripe { position: absolute; left: 0; right: 0; top: 314px; height: 3px; background: var(--navy); }
  .base-band { position: absolute; left: 0; right: 0; top: 317px; bottom: 0; background: var(--band); }
</style>
</head>
<body>

  <section class="card card--back" aria-label="Card back">
    <div class="brand">
      <span class="brand__dot"></span>
      <div>
        <div class="brand__name">Orvane Diamonds</div>
        <div class="brand__tagline">Import-Export of Rough-Polished Diamonds</div>
        <div class="brand__suffix">b.v.b.a</div>
      </div>
    </div>
  </section>

  <section class="card card--front" aria-label="Card front">
    <div class="brand">
      <span class="brand__dot"></span>
      <div>
        <div class="brand__name">Orvane Diamonds</div>
        <div class="brand__tagline">Import-Export of Rough-Polished Diamonds</div>
        <div class="brand__suffix">b.v.b.a</div>
      </div>
    </div>

    <div class="divider"></div>

    <ul class="contact">
      <li>
        <svg viewBox="0 0 24 24" aria-hidden="true"><path d="M6.6 10.8a15.1 15.1 0 0 0 6.6 6.6l2.2-2.2a1 1 0 0 1 1-.25 11.4 11.4 0 0 0 3.6.57 1 1 0 0 1 1 1V20a1 1 0 0 1-1 1A17 17 0 0 1 3 4a1 1 0 0 1 1-1h3.5a1 1 0 0 1 1 1c0 1.25.2 2.45.57 3.6a1 1 0 0 1-.25 1z"/></svg>
        0208-555-0147
      </li>
      <li>
        <svg viewBox="0 0 24 24" aria-hidden="true"><path d="M12 2a10 10 0 1 0 5 18.7l-1-1.7A8 8 0 1 1 20 12v1.5a1.5 1.5 0 0 1-3 0V12a5 5 0 1 0-1.5 3.6A3.5 3.5 0 0 0 22 13.5V12A10 10 0 0 0 12 2zm0 13a3 3 0 1 1 0-6 3 3 0 0 1 0 6z"/></svg>
        marcus@orvanediamonds.com
      </li>
      <li>
        <svg viewBox="0 0 24 24" aria-hidden="true"><path d="M12 2a10 10 0 1 0 0 20 10 10 0 0 0 0-20zm6.9 6h-2.9a15.6 15.6 0 0 0-1.4-3.6A8 8 0 0 1 18.9 8zM12 4c.8 1.2 1.5 2.5 1.9 4h-3.8c.4-1.5 1.1-2.8 1.9-4zM4.3 14a8 8 0 0 1 0-4h3.4a16 16 0 0 0 0 4zm.8 2h2.9c.3 1.3.8 2.5 1.4 3.6A8 8 0 0 1 5.1 16zM8 8H5.1a8 8 0 0 1 4.3-3.6C8.8 5.5 8.3 6.7 8 8zm4 12c-.8-1.2-1.5-2.5-1.9-4h3.8c-.4 1.5-1.1 2.8-1.9 4zm2.3-6H9.7a14.6 14.6 0 0 1 0-4h4.6a14.6 14.6 0 0 1 0 4zm.3 5.6c.6-1.1 1.1-2.3 1.4-3.6h2.9a8 8 0 0 1-4.3 3.6zm1.7-5.6a16 16 0 0 0 0-4h3.4a8 8 0 0 1 0 4z"/></svg>
        www.orvanediamonds.com
      </li>
    </ul>

    <div class="person">
      <div class="person__name">MARCUS HALE</div>
      <div class="person__role">Export Manager</div>
      <div class="person__rule"></div>
    </div>

    <address class="address" style="font-style: normal;">
      48 Fenwick Lane,<br>
      Ashbury-Upon-Wey,<br>
      KT9 3LR
    </address>

    <div class="stripe"></div>
    <div class="base-band"></div>
  </section>

</body>
</html>
```